Korvex App's Dashboard Redesign

We are redesigning our existing Korvex app (http://www.tamselo.com) to use Korvex's new Plinth Layout guidelines (read more here: http://www.brindlework.com/design/).

We would like to see new designs of the app's main screen (see tamselo_dashboard.png) from you.

The new dashboard screen design should:
A. follow Korvex's new Plinth Layout guidelines
B. contain an actionbar at the top (with an icon for hints and a "hamburger menu icon" on the left)
C. contain 4 buttons to the app's other screens: 1. Edit today's symptoms, 2. Calendar view, 3. Timeline view, 4. Chart view. (Please, do not put the buttons into tabs, as we want to avoid putting tabs on other screens too)
D. keep the basic concept of the cycle wheel (circle/donut representing the days of cycle; distinguish passed/upcoming days of cycle; show current cycle day; show menses days/fertile days/ovulation day)
E. contain iconic or textual predictions of the number of days to the next menses/ovulation
F. be easily themable to different colors (as the app supports more color themes)

To get a better idea about the app in general and the dashboard/cycle wheel in particular, please install the app and read Petal Loop Guides. This will help you understand the functional requirements.

Wheel

```html
<!DOCTYPE html>
<html lang="en">
<head>
<meta charset="utf-8">
<title>Korvex Dashboard – Fertile phase</title>
<link rel="stylesheet" href="https://fonts.googleapis.com/css2?family=Roboto:wght@400;500&display=swap">
<style>
  :root {
    --status-bar: #C2185B;
    --app-bar: #EC407A;
    --surface: #FAFAFA;
    --nav-bar: #000000;
    --on-primary: #FFFFFF;
    --ring-upcoming: #FF82A9;
    --fertile-light: #B388FF;
    --fertile-deep: #7C4DFF;
    --menses: #EC407A;
    --text-main: #424242;
    --dot-active: #757575;
    --dot-idle: #C4C4C4;
    --divider: #8A8A8A;
  }
  html, body {
    margin: 0;
    padding: 0;
    width: 1200px;
    height: 1064px;
    overflow: hidden;
    background: var(--surface);
    font-family: "Roboto", sans-serif;
  }
  .board {
    display: flex;
    width: 1200px;
    height: 1064px;
  }
  .screen {
    width: 598px;
    height: 1064px;
    display: block;
    flex: none;
  }
  .screen-divider {
    width: 4px;
    height: 1064px;
    background: var(--divider);
    flex: none;
  }
  .status-bar { fill: var(--status-bar); }
  .app-bar { fill: var(--app-bar); }
  .body-area { fill: var(--surface); }
  .nav-bar { fill: var(--nav-bar); }
  .on-primary { fill: var(--on-primary); }
  .nav-icon { fill: none; stroke: var(--on-primary); stroke-width: 2.6; stroke-linejoin: round; }
  .status-time { fill: var(--on-primary); font-size: 18px; font-weight: 400; }
  .screen-title { fill: var(--on-primary); font-size: 28px; font-weight: 500; }
  .ring-base { fill: none; stroke: var(--ring-upcoming); stroke-width: 58; }
  .ring-fertile { fill: none; stroke: var(--fertile-light); stroke-width: 48; stroke-linecap: round; }
  .ring-peak-thin { fill: none; stroke: var(--fertile-deep); stroke-width: 34; stroke-linecap: round; }
  .ring-peak-thick { fill: none; stroke: var(--fertile-deep); stroke-width: 58; stroke-linecap: round; }
  .ring-menses { fill: none; stroke: var(--menses); stroke-width: 56; stroke-linecap: round; }
  .day-pin { fill: var(--fertile-deep); }
  .day-pin-label { fill: var(--on-primary); font-size: 36px; font-weight: 400; }
  .countdown-icon { fill: var(--fertile-deep); }
  .countdown-value { fill: var(--text-main); font-size: 38px; font-weight: 400; }
  .pager-dot { fill: var(--dot-idle); }
  .pager-dot.is-active { fill: var(--dot-active); }
  .fab { fill: var(--menses); }
</style>
</head>
<body>
<svg width="0" height="0" style="position:absolute" aria-hidden="true">
  <defs>
    <symbol id="icon-flower" viewBox="-12 -12 24 24">
      <g fill="#FFFFFF">
        <ellipse cx="0" cy="-6.5" rx="2.6" ry="4"/>
        <ellipse cx="0" cy="-6.5" rx="2.6" ry="4" transform="rotate(45)"/>
        <ellipse cx="0" cy="-6.5" rx="2.6" ry="4" transform="rotate(90)"/>
        <ellipse cx="0" cy="-6.5" rx="2.6" ry="4" transform="rotate(135)"/>
        <ellipse cx="0" cy="-6.5" rx="2.6" ry="4" transform="rotate(180)"/>
        <ellipse cx="0" cy="-6.5" rx="2.6" ry="4" transform="rotate(225)"/>
        <ellipse cx="0" cy="-6.5" rx="2.6" ry="4" transform="rotate(270)"/>
        <ellipse cx="0" cy="-6.5" rx="2.6" ry="4" transform="rotate(315)"/>
      </g>
      <circle r="2.6" fill="#7C4DFF"/>
    </symbol>
    <symbol id="icon-flower-small" viewBox="-12 -12 24 24">
      <g fill="#FFFFFF">
        <ellipse cx="0" cy="-5.5" rx="3" ry="3.6"/>
        <ellipse cx="0" cy="-5.5" rx="3" ry="3.6" transform="rotate(72)"/>
        <ellipse cx="0" cy="-5.5" rx="3" ry="3.6" transform="rotate(144)"/>
        <ellipse cx="0" cy="-5.5" rx="3" ry="3.6" transform="rotate(216)"/>
        <ellipse cx="0" cy="-5.5" rx="3" ry="3.6" transform="rotate(288)"/>
      </g>
      <circle r="1.8" fill="#B388FF"/>
    </symbol>
    <symbol id="icon-drop" viewBox="-10 -14 20 28">
      <path d="M0 -13 C5 -5 9 0 9 5 A9 9 0 0 1 -9 5 C-9 0 -5 -5 0 -13 Z"/>
    </symbol>
    <symbol id="icon-edit" viewBox="0 0 24 24">
      <path fill="#FFFFFF" d="M3 17.25V21h3.75L17.81 9.94l-3.75-3.75L3 17.25zM20.71 7.04a1 1 0 0 0 0-1.41l-2.34-2.34a1 1 0 0 0-1.41 0l-1.83 1.83 3.75 3.75 1.83-1.83z"/>
    </symbol>
    <symbol id="icon-hint" viewBox="0 0 36 36">
      <g fill="#FFFFFF">
        <path d="M18 9a8 8 0 0 0-4.8 14.4V26h9.6v-2.6A8 8 0 0 0 18 9z"/>
        <rect x="13.8" y="27.4" width="8.4" height="2.4" rx="1"/>
        <rect x="15" y="31" width="6" height="2.2" rx="1"/>
        <rect x="16.8" y="1.5" width="2.4" height="4.2" rx="1"/>
        <rect x="16.8" y="1.5" width="2.4" height="4.2" rx="1" transform="rotate(-45 18 18)"/>
        <rect x="16.8" y="1.5" width="2.4" height="4.2" rx="1" transform="rotate(45 18 18)"/>
        <rect x="16.8" y="1.5" width="2.4" height="4.2" rx="1" transform="rotate(-90 18 18)"/>
        <rect x="16.8" y="1.5" width="2.4" height="4.2" rx="1" transform="rotate(90 18 18)"/>
      </g>
    </symbol>
    <symbol id="screen-content" viewBox="0 0 540 960">
      <!-- status bar -->
      <rect class="status-bar" x="0" y="0" width="540" height="36"/>
      <path class="on-primary" d="M377 14 Q388 6 399 14 L388 27 Z"/>
      <path class="on-primary" d="M432 11 V28 H415 Z"/>
      <rect class="on-primary" x="453" y="11" width="11" height="17" rx="1.5"/>
      <text class="status-time" x="528" y="26" text-anchor="end">12:30</text>

      <!-- app bar -->
      <rect class="app-bar" x="0" y="36" width="540" height="84"/>
      <g class="on-primary">
        <rect x="28" y="70" width="28" height="3"/>
        <rect x="28" y="78.5" width="28" height="3"/>
        <rect x="28" y="87" width="28" height="3"/>
      </g>
      <text class="screen-title" x="107" y="89">Fertile phase</text>
      <path class="on-primary" d="M293 77 H306 L299.5 83.5 Z"/>
      <use href="#icon-hint" x="480" y="60" width="36" height="36"/>

      <!-- body -->
      <rect class="body-area" x="0" y="120" width="540" height="768"/>

      <!-- cycle wheel -->
      <circle class="ring-base" cx="270" cy="522" r="163"/>
      <path class="ring-menses" d="M195 663.3 A160 160 0 0 1 132.9 604.4"/>
      <path class="ring-fertile" d="M109.6 499.5 A162 162 0 0 1 414.3 448.5"/>
      <path class="ring-peak-thin" d="M299.2 356.5 A168 168 0 0 1 371.1 387.8"/>
      <path class="ring-peak-thick" d="M177.7 395 A157 157 0 0 1 286 365"/>
      <use href="#icon-flower" x="289" y="356" width="28" height="28"/>
      <use href="#icon-flower-small" x="96" y="489" width="22" height="22"/>
      <use href="#icon-drop" class="on-primary" x="181" y="652" width="19" height="27"/>

      <!-- current day pin -->
      <path class="day-pin" d="M270 309 L239 278 A44 44 0 1 1 301 278 Z"/>
      <text class="day-pin-label" x="270" y="260" text-anchor="middle">14</text>

      <!-- days to next event -->
      <use href="#icon-drop" class="countdown-icon" x="224" y="511" width="26" height="37"/>
      <text class="countdown-value" x="270" y="542">17</text>

      <!-- pager -->
      <circle class="pager-dot is-active" cx="252" cy="642" r="4.5"/>
      <circle class="pager-dot" cx="270" cy="642" r="4.5"/>
      <circle class="pager-dot" cx="288" cy="642" r="4.5"/>

      <!-- edit today -->
      <circle class="fab" cx="474" cy="822" r="42"/>
      <use href="#icon-edit" x="457" y="805" width="34" height="34"/>

      <!-- navigation bar -->
      <rect class="nav-bar" x="0" y="888" width="540" height="72"/>
      <path class="nav-icon" d="M130 912 V934 L110 923 Z"/>
      <circle class="nav-icon" cx="268" cy="923" r="11"/>
      <rect class="nav-icon" x="408" y="913" width="20" height="20" rx="1"/>
    </symbol>
  </defs>
</svg>

<main class="board">
  <svg class="screen screen-primary" viewBox="0 0 540 960" role="group" aria-label="Dashboard, fertile phase">
    <use href="#screen-content" x="0" y="0" width="540" height="960"/>
  </svg>
  <div class="screen-divider"></div>
  <svg class="screen screen-variant" viewBox="0 0 540 960" role="group" aria-label="Dashboard, fertile phase variant">
    <use href="#screen-content" x="0" y="0" width="540" height="960"/>
  </svg>
</main>
</body>
</html>
```